Modernise Business Card

Our company has been operating for 10 years. With the start of the new decade we are looking to refresh our business card design. We manufacture a range of industrial product shipping to customers internationally. A copy of our current card, both sides, is attached. We are looking for a mature professional appearance.

```html
<!DOCTYPE html>
<html lang="en">
<head>
<meta charset="utf-8">
<title>Veltrix Business Card – Front and Back</title>
<link href="https://fonts.googleapis.com/css2?family=Jost:wght@400;600&display=swap" rel="stylesheet">
<style>
  :root {
    --brand-blue: #1aa3d6;
    --ink: #111111;
    --frame-black: #231f20;
    --card-white: #ffffff;
    --backdrop: #d9dcdd;
  }
  * { box-sizing: border-box; margin: 0; padding: 0; }
  html, body { width: 1200px; height: 1200px; overflow: hidden; }
  body {
    background: var(--backdrop);
    font-family: "Jost", "Century Gothic", sans-serif;
    color: var(--ink);
    position: relative;
  }
  .card {
    position: absolute;
    left: 250px;
    width: 700px;
    height: 400px;
    background: var(--card-white);
    box-shadow: 0 6px 18px rgba(0,0,0,0.12);
  }
  .card--front { top: 170px; }
  .card--back { top: 630px; border: 47px solid var(--frame-black); }

  .brand-name {
    font-family: "Jost", sans-serif;
    font-weight: 600;
    color: var(--brand-blue);
    letter-spacing: 0.5px;
    line-height: 1;
  }
  .card--front .brand-name {
    position: absolute;
    right: 62px;
    top: 50px;
    font-size: 46px;
  }
  .holder-name {
    position: absolute;
    left: 80px;
    top: 62px;
    font-size: 34px;
    font-weight: 600;
    line-height: 1.2;
  }
  .contact-row {
    position: absolute;
    left: 78px;
    display: flex;
    align-items: center;
    gap: 14px;
    font-size: 19px;
    line-height: 26px;
  }
  .contact-row .icon { width: 34px; height: 34px; flex: none; }
  .row-phone { top: 128px; }
  .row-email { top: 204px; }
  .row-address { top: 246px; }
  .row-web { top: 333px; }

  .card--back .inner {
    position: absolute;
    inset: 0;
  }
  .card--back .brand-name,
  .product-lines,
  .back-web {
    position: absolute;
    left: 0;
    right: 0;
    text-align: center;
  }
  .card--back .brand-name { top: 72px; font-size: 46px; }
  .product-lines {
    top: 160px;
    list-style: none;
    color: var(--brand-blue);
    font-size: 20px;
    line-height: 28px;
    text-transform: uppercase;
  }
  .back-web { top: 256px; font-size: 16px; line-height: 22px; }
</style>
</head>
<body>

<section class="card card--front" aria-label="Business card front">
  <h1 class="holder-name">Ewan Forsyth</h1>
  <div class="brand-name">Veltrix</div>

  <div class="contact-row row-phone">
    <svg class="icon" viewBox="0 0 34 34" aria-hidden="true">
      <circle cx="17" cy="17" r="17" fill="var(--brand-blue)"/>
      <path d="M11 10.5c1-1 2.2-1 2.8 0l1.6 2.6c.4.7.2 1.5-.4 2l-1 .8c.8 1.9 2.3 3.4 4.1 4.2l.8-1c.5-.6 1.3-.8 2-.4l2.6 1.6c1 .6 1 1.8 0 2.8l-1.2 1.2c-1 1-3 1.1-5.3-.4-2.5-1.6-4.9-4-6.5-6.5-1.5-2.3-1.4-4.3-.4-5.3z" fill="#fff"/>
    </svg>
    <div>China: +86 155 2037 6418<br>Australia: +61 412 738 905</div>
  </div>

  <div class="contact-row row-email">
    <svg class="icon" viewBox="0 0 34 34" aria-hidden="true">
      <circle cx="17" cy="17" r="17" fill="var(--brand-blue)"/>
      <rect x="9" y="11.5" width="16" height="11" fill="none" stroke="#fff" stroke-width="1.8"/>
      <path d="M9 11.5l8 6.5 8-6.5" fill="none" stroke="#fff" stroke-width="1.8"/>
    </svg>
    <div>eforsyth@veltrixfittings.com</div>
  </div>

  <div class="contact-row row-address">
    <svg class="icon" viewBox="0 0 34 34" aria-hidden="true">
      <circle cx="17" cy="17" r="17" fill="var(--brand-blue)"/>
      <path d="M17 7.5c-3.6 0-6.3 2.7-6.3 6.2 0 4.4 6.3 12.2 6.3 12.2s6.3-7.8 6.3-12.2c0-3.5-2.7-6.2-6.3-6.2z" fill="#fff"/>
      <circle cx="17" cy="13.8" r="2.4" fill="var(--brand-blue)"/>
    </svg>
    <div>908-3, Lanting Trade Tower<br>417 Qingshan Road, Haishu District<br>Ningbo 315000 China</div>
  </div>

  <div class="contact-row row-web">
    <svg class="icon" viewBox="0 0 34 34" aria-hidden="true">
      <circle cx="17" cy="17" r="17" fill="var(--brand-blue)"/>
      <g fill="none" stroke="#fff" stroke-width="1.5">
        <circle cx="17" cy="17" r="8"/>
        <ellipse cx="17" cy="17" rx="3.5" ry="8"/>
        <path d="M9 17h16M10.2 13h13.6M10.2 21h13.6"/>
      </g>
    </svg>
    <div>www.veltrixfittings.com</div>
  </div>
</section>

<section class="card card--back" aria-label="Business card back">
  <div class="inner">
    <div class="brand-name">Veltrix</div>
    <ul class="product-lines">
      <li>Hydraulic Adapters</li>
      <li>Hose Fittings</li>
      <li>Quick Couplings</li>
    </ul>
    <div class="back-web">www.veltrixfittings.com</div>
  </div>
</section>

</body>
</html>
```